Cedar Hollow Drift Tours

We offer guided cross country ( Nordic ) skiing tours in the National Forest bordering Yellowstone National Park. I need a website that attracts individuals by using photos ( provided by me ) , brief descriptions of what to expect, a place with phone numbers to call for a tour, and I would like the website to feature the same color scheme as the logo, which I will upload.

```html
<!DOCTYPE html>
<html lang="en">
<head>
<meta charset="utf-8">
<title>Cedar Hollow Drift Tours</title>
<link href="https://fonts.googleapis.com/css2?family=Montserrat:wght@400;500;600;700&family=Arimo:ital,wght@0,400;1,400&display=swap" rel="stylesheet">
<style>
:root{
  --brand:#5470b6;
  --brand-dark:#3f5aa0;
  --ink:#111111;
  --text:#555a66;
  --white:#ffffff;
  --sky-top:#1f3d7a;
  --sky-mid:#5b7fb8;
  --snow:#e6ebf2;
  --rock:#5c6472;
  --forest:#3e444c;
}
*{box-sizing:border-box;margin:0;padding:0}
html,body{width:1200px;height:3640px;overflow:hidden}
body{position:relative;background:var(--white);font-family:"Montserrat",sans-serif;color:var(--ink)}
.abs{position:absolute}

/* hero */
.hero{left:0;top:0;width:1200px;height:766px;
  background:linear-gradient(180deg,var(--sky-top) 0%,var(--sky-mid) 30%,#8fa6c6 42%,var(--snow) 58%,#b9c1cc 72%,var(--rock) 100%)}
.nav{left:112px;top:68px;width:977px;height:82px;background:var(--white);border-radius:41px}
.nav a{position:absolute;top:32px;font-size:14px;font-weight:500;color:var(--ink);text-decoration:none;letter-spacing:.2px}
.brand-badge{left:503px;top:22px;width:176px;height:176px;border-radius:50%;background:var(--white);
  display:flex;align-items:center;justify-content:center;text-align:center}
.brand-badge span{font-size:15px;font-weight:700;color:var(--brand);line-height:1.35;width:120px}
.hero-title{left:0;top:270px;width:1200px;text-align:center;color:var(--white);font-size:35px;font-weight:700;letter-spacing:.3px}
.hero-sub{left:250px;top:326px;width:700px;text-align:center;color:var(--white);font-size:19.5px;line-height:30px}
.btn-outline{display:flex;align-items:center;justify-content:center;border:2px solid var(--white);border-radius:30px;
  color:var(--white);font-weight:500;letter-spacing:.3px}
.hero-btn{left:497px;top:406px;width:204px;height:58px;font-size:17.5px}

/* photo strip */
.card{top:725px;width:232px;height:314px;background:var(--white);padding:5px}
.card .ph{width:100%;height:100%}
.card-cta{position:absolute;left:0;bottom:22px;width:100%;text-align:center;color:var(--white);font-size:17px;font-weight:500;text-decoration:underline}

/* about */
.about-ring{left:150px;top:1129px;width:430px;height:430px;border-radius:50%;border:3px solid var(--brand)}
.about-photo{left:160px;top:1139px;width:410px;height:410px;border-radius:50%;background:radial-gradient(circle at 50% 45%,#e8e8e8,#a9a9a9 70%,#8a8a8a)}
.section-title{color:var(--brand);font-size:40px;font-weight:600;letter-spacing:.3px}
.rule{height:4px;background:var(--brand);width:66px}
.para{font-family:"Arimo",sans-serif;color:var(--text);font-size:13.5px;text-align:justify}
.btn-solid{display:flex;align-items:center;justify-content:center;background:var(--brand);color:var(--white);border-radius:30px;font-size:16px;font-weight:500}

/* banner */
.banner{left:0;top:1642px;width:1200px;height:550px;background:linear-gradient(180deg,#9aa2aa 0%,#6e767e 35%,var(--forest) 75%,#2b2f34 100%)}
.banner-h1{left:0;top:1790px;width:1200px;text-align:center;color:var(--white);font-size:62px;font-weight:600;letter-spacing:1px}
.banner-h2{left:0;top:1862px;width:1200px;text-align:center;color:var(--white);font-size:44px;font-weight:500;letter-spacing:.5px}
.banner-tag{left:0;top:1930px;width:1200px;text-align:center;color:var(--white);font-size:24px;font-weight:600;letter-spacing:.5px}
.banner-btn{left:483px;top:1989px;width:234px;height:56px;font-size:18px}

/* expect */
.expect-art{left:127px;top:2271px;width:452px;height:452px;border-radius:50%;border:13px solid #1c1a1c;
  background:linear-gradient(180deg,#b3c4ea 0%,#c9d5ef 45%,#e8eaee 70%,#d8dade 100%)}

/* testimonial */
.testimonial{left:0;top:2777px;width:1200px;height:399px;background:var(--brand)}
.avatar{left:538px;top:2827px;width:122px;height:122px;border-radius:50%;background:radial-gradient(circle at 50% 40%,#c78f72,#7a4a35 75%)}
.arrow-box{top:2961px;width:43px;height:41px;border:1.5px solid var(--white);display:flex;align-items:center;justify-content:center}
.quote{left:250px;top:2962px;width:700px;text-align:center;color:var(--white);font-family:"Arimo",sans-serif;font-style:italic;font-size:15.5px;line-height:27.5px}
.quote-mark{font-family:Georgia,serif;font-style:normal;font-weight:700;font-size:44px;line-height:0;vertical-align:-14px}
.author{left:0;top:3090px;width:1200px;text-align:center;color:var(--white);font-size:19px;font-weight:500;letter-spacing:.5px}

/* footer */
.footer{left:0;top:3176px;width:1200px;height:464px;background:var(--ink)}
.foot-nav a{position:absolute;top:3210px;color:var(--white);font-size:14px;text-decoration:none}
.foot-line{left:112px;top:3258px;width:977px;height:1px;background:#2a2a2a}
.foot-title{top:3298px;color:var(--white);font-size:17px;font-weight:600;letter-spacing:.3px}
.field{background:var(--white);font-family:"Arimo",sans-serif;font-size:11px;color:#333;padding:12px 13px}
.submit{left:110px;top:3499px;width:99px;height:34px;background:var(--brand);color:var(--white);font-family:"Arimo",sans-serif;font-size:13px;display:flex;align-items:center;justify-content:center}
.icon{left:553px;width:42px;height:42px;border:1.5px solid var(--white);border-radius:50%;display:flex;align-items:center;justify-content:center}
.info-label{left:611px;color:var(--white);font-size:15px;font-weight:500}
.info-val{left:611px;color:var(--white);font-family:"Arimo",sans-serif;font-size:13px}
.foot-badge{left:851px;top:3320px;width:200px;height:200px;border-radius:50%;background:var(--white);display:flex;align-items:center;justify-content:center;text-align:center}
.foot-badge span{font-size:17px;font-weight:700;color:var(--brand);line-height:1.4;width:140px}
.copyright{left:0;top:3591px;width:1200px;text-align:center;color:var(--white);font-family:"Arimo",sans-serif;font-size:14px}
</style>
</head>
<body>

<!-- hero -->
<div class="abs hero" role="img" aria-label="Snow-covered mountain peak under a deep blue sky with clouds"></div>
<nav class="abs nav">
  <a style="left:31px">HOME</a>
  <a style="left:130px">ABOUT ME</a>
  <a style="left:262px">PROJECT</a>
  <a style="left:602px">WHAT TO EXPECT</a>
  <a style="left:783px">NEWS</a>
  <a style="left:883px">CONTACT</a>
</nav>
<div class="abs brand-badge"><span>CEDAR HOLLOW DRIFT TOURS</span></div>
<h1 class="abs hero-title">CEDAR HOLLOW DRIFT TOURS</h1>
<p class="abs hero-sub">Sed ut perspiciatis unde omnis iste natus error sit voluptatem sit unde unde omnis&nbsp; accusantium doloremque</p>
<div class="abs btn-outline hero-btn">READ MORE</div>

<!-- photo strip -->
<div class="abs card" style="left:112px">
  <div class="ph" role="img" aria-label="Skier on a trail between snow-laden pine trees" style="background:linear-gradient(180deg,#9fb4cf 0%,#d9dee4 35%,#6f7a72 60%,#eef1f4 100%)"></div>
  <div class="card-cta">CALL FOR A TOUR</div>
</div>
<div class="abs card" style="left:362px">
  <div class="ph" role="img" aria-label="Rocky mountain peak glowing orange at sunset" style="background:linear-gradient(180deg,#7d8f96 0%,#8d9598 35%,#d98a3f 50%,#8a5a3a 70%,#2f3438 100%)"></div>
</div>
<div class="abs card" style="left:608px">
  <div class="ph" role="img" aria-label="Snowy forest clearing with tall evergreens" style="background:linear-gradient(180deg,#aab4c4 0%,#c7ccd4 40%,#59635f 65%,#e4e8ee 100%)"></div>
</div>
<div class="abs card" style="left:855px">
  <div class="ph" role="img" aria-label="Groomed snow trail through a pine forest under blue sky" style="background:linear-gradient(180deg,#7d9ccb 0%,#c9d3df 30%,#3f5044 55%,#f2f5f9 100%)"></div>
</div>

<!-- about -->
<div class="abs about-ring"></div>
<div class="abs about-photo" role="img" aria-label="Portrait of the tour guide in a blazer, pointing toward the text"></div>
<h2 class="abs section-title" style="left:642px;top:1128px">ABOUT ME</h2>
<div class="abs rule" style="left:642px;top:1186px"></div>
<p class="abs para" style="left:642px;top:1214px;width:407px;line-height:27.4px">Sed ut perspiciatis unde omnis iste natus error sit voluptatem accusantium doloremque laudantium, totam rem aperiam, eaque ipsa quae ab illo inventore veritatis et quasi architecto beatae vitae dicta sunt explicabo. Nemo enim ipsam voluptatem quia voluptas sit aspernatur aut odit aut fugit, sed quia consequuntur magni dolores eos qui ratione voluptatem sequi nesciunt. Neque porro quisquam est, qui dolorem ipsum quia dolor sit amet, consectetur, adipisci vet dolore magnam aliquam quaerat voluptatem.</p>
<div class="abs btn-solid" style="left:642px;top:1457px;width:154px;height:55px">READ MORE</div>

<!-- banner -->
<div class="abs banner" role="img" aria-label="Misty snowy pine forest on a mountainside"></div>
<div class="abs banner-h1">CEDAR HOLLOW</div>
<div class="abs banner-h2">DRIFT TOURS</div>
<div class="abs banner-tag">SED UT PERSPICIATIS UNDE OMNIS ISTE NATUS ERROR</div>
<div class="abs btn-outline banner-btn">CALL FOR A TOUR</div>

<!-- what to expect -->
<div class="abs expect-art" role="img" aria-label="Illustration of a cross-country skier in front of a snowy mountain and pine tree"></div>
<h2 class="abs section-title" style="left:626px;top:2310px">WHAT TO EXPECT</h2>
<div class="abs rule" style="left:626px;top:2367px"></div>
<p class="abs para" style="left:630px;top:2403px;width:441px;line-height:25.8px">Sed ut perspiciatis unde omnis iste natus error sit voluptatem accusantium doloremque laudantium, totam rem aperiam, eaque ipsa quae ab illo inventore veritatis et quasi architecto beatae vitae dicta sunt explicabo. Nemo enim ipsam voluptatem quia voluptas sit aspernatur aut odit aut fugit, sed quia consequuntur magni dolores eos qui ratione voluptatem totam rem aperiam, eaque i sequi nesciunt.</p>
<div class="abs btn-solid" style="left:630px;top:2592px;width:174px;height:59px">LEARN MORE</div>

<!-- testimonial -->
<div class="abs testimonial"></div>
<div class="abs avatar" role="img" aria-label="Portrait of a smiling guest"></div>
<div class="abs arrow-box" style="left:171px">
  <svg width="10" height="14" viewBox="0 0 10 14"><path d="M7 2 L2 7 L7 12" fill="none" stroke="#fff" stroke-width="1.8"/></svg>
</div>
<div class="abs arrow-box" style="left:985px">
  <svg width="10" height="14" viewBox="0 0 10 14"><path d="M3 2 L8 7 L3 12" fill="none" stroke="#fff" stroke-width="1.8"/></svg>
</div>
<p class="abs quote"><span class="quote-mark">&#8220;</span> Sed ut perspiciatis unde omnis iste natus error sit voluptatem accusantium doloremque laudantium, totam rem aperiam, eaque ipsa quae ab illo inventore veritatis et quasi architecto beatae vitae dicta sunt explicabo. Nemo enim ipsam voluptatem quia voluptas sit aspernatur aut odit aut fugit, sed quia consequuntur magni dolores eos qui ratione voluptatem sequi nesciunt. <span class="quote-mark">&#8221;</span></p>
<div class="abs author">-MARA LINDEN</div>

<!-- footer -->
<footer class="abs footer"></footer>
<div class="foot-nav">
  <a style="left:238px">HOME</a>
  <a style="left:342px">ABOUT ME</a>
  <a style="left:478px">PROJECT</a>
  <a style="left:603px">WHAT TO EXPECT</a>
  <a style="left:789px">NEWS</a>
  <a style="left:892px">CONTACT</a>
</div>
<div class="abs foot-line"></div>

<div class="abs foot-title" style="left:113px">CONTACT US</div>
<div class="abs field" style="left:113px;top:3348px;width:180px;height:35px">First Name :</div>
<div class="abs field" style="left:303px;top:3348px;width:180px;height:35px">Last Name :</div>
<div class="abs field" style="left:113px;top:3393px;width:180px;height:35px">Email :</div>
<div class="abs field" style="left:303px;top:3393px;width:180px;height:35px">Phone :</div>
<div class="abs field" style="left:113px;top:3438px;width:370px;height:53px">Message :</div>
<div class="abs submit">SUBMIT</div>

<div class="abs foot-title" style="left:561px">ADDRESS</div>
<div class="abs icon" style="top:3344px">
  <svg width="16" height="18" viewBox="0 0 16 18"><path d="M8 1 C4.5 1 2.5 3.5 2.5 6.5 C2.5 10.5 8 17 8 17 C8 17 13.5 10.5 13.5 6.5 C13.5 3.5 11.5 1 8 1 Z" fill="none" stroke="#fff" stroke-width="1.6"/><circle cx="8" cy="6.5" r="2" fill="#fff"/></svg>
</div>
<div class="abs info-label" style="top:3349px">ADDRESS</div>
<div class="abs info-val" style="top:3370px"># 125 Lorem Ipsum Dummy</div>

<div class="abs icon" style="top:3407px">
  <svg width="16" height="16" viewBox="0 0 16 16"><path d="M4 1.5 L6 5 L4.6 6.6 C5.5 8.6 7.4 10.5 9.4 11.4 L11 10 L14.5 12 L13.2 14.3 C7.5 14 2 8.5 1.7 2.8 Z" fill="#fff"/></svg>
</div>
<div class="abs info-label" style="top:3411px">PHONE</div>
<div class="abs info-val" style="top:3433px">000-121-1213</div>

<div class="abs icon" style="top:3473px">
  <svg width="16" height="12" viewBox="0 0 16 12"><rect x="1" y="1" width="14" height="10" rx="1" fill="#fff"/><path d="M1.5 1.5 L8 6.5 L14.5 1.5" fill="none" stroke="#111" stroke-width="1.4"/></svg>
</div>
<div class="abs info-label" style="top:3475px">EMAIL</div>
<div class="abs info-val" style="top:3497px">hello@cedarhollowdrift.example</div>

<div class="abs foot-badge"><span>CEDAR HOLLOW DRIFT TOURS</span></div>

<div class="abs copyright">© Copyright 2021 Cedar Hollow Drift Tours.All Rights Reserved</div>

</body>
</html>
```